Website for Company to help with House Restoration from Hurricane Damage

Crisp, Clean and Professional!

I need a FRONT page for a website. I need it created in photoshop with the layers intact. We DO NOT need the HTML or DRB for the site. Simply the design. Any fonts you use will need to be included if they are not standard. Please make sure any fonts you use in the body of the text are available for use on Google Fonts.

I have attached a word doc that lists the menu items and additional instructions.

A little about the company - after Hurricane Marlow - DRB developed a system which allows the house to be raised, the Tremlets installed, and the house reset on the Tremlets without the expense of moving the house or driving new pilings. This option can be installed in a matter of days with limited space and at a lower construction cost.

Please refer to the attached musthaves.doc and images that are included.

The main page must incorporate the menu, the attached photos w/ text underneath (text is in the word doc attached), and the text included in the word doc.

Standard footer with contact info as well.

If you have questions please contact us!
Updates

Designs are due by Friday! We will pick one this weekend.  We are unable to change it from 10 days to 5.  Thank you!!!

Target Market(s)

People who lost their homes or businesses due to a hurricane.

Industry/Entity Type

Construction

Requirements
Must have
• See attached musthaves.doc

```html
<!DOCTYPE html>
<html lang="en">
<head>
<meta charset="utf-8">
<title>DRB – Durable Raise Builders</title>
<link rel="stylesheet" href="https://fonts.googleapis.com/css2?family=Source+Sans+3:ital,wght@0,400;0,600;1,600&family=PT+Serif&display=swap">
<style>
:root{
  --bg-top:#c5d5a2;
  --bg-bottom:#758f52;
  --panel:#fdfdfc;
  --green:#6f8a3f;
  --green-light:#a9c17b;
  --green-dark:#6c8744;
  --ink:#2b2b22;
  --body:#3c3c36;
  --rule:#d9ddd0;
  --white:#ffffff;
}
*{margin:0;padding:0;box-sizing:border-box}
html,body{width:1200px;height:1175px;overflow:hidden}
body{
  position:relative;
  background:linear-gradient(180deg,var(--bg-top) 0%,#a8bf80 45%,var(--bg-bottom) 100%);
  font-family:"Source Sans 3",sans-serif;color:var(--body);
}
.page{position:absolute;left:120px;top:30px;width:960px;height:953px;background:var(--panel);box-shadow:0 0 6px rgba(0,0,0,.15)}
.brand{position:absolute;left:17px;top:22px;width:100px;height:108px;display:flex;align-items:center;gap:8px}
.brand-dot{width:22px;height:22px;border-radius:50%;background:var(--green)}
.brand-name{font-size:34px;font-weight:600;color:var(--green)}
.social{position:absolute;right:12px;top:32px;display:flex;gap:5px}
.social span{width:27px;height:27px;border-radius:4px;background:#9aa98a}
.search{position:absolute;left:718px;top:80px;width:228px;height:34px;border:1px solid #cfd3c7;border-radius:3px;background:linear-gradient(#fff,#f1f2ee)}
.search em{position:absolute;left:12px;top:9px;font-size:12px;color:#8a8a80}
.search svg{position:absolute;right:8px;top:6px}
.nav{position:absolute;left:10px;top:146px;width:940px;height:49px;border-radius:3px;
  background:linear-gradient(#b7cc8e,#8eaa5f 55%,#7a964d);display:flex;box-shadow:0 1px 2px rgba(0,0,0,.25)}
.nav a{display:block;height:49px;line-height:50px;font-size:17px;color:var(--ink);text-decoration:none;text-align:center;border-right:1px solid #6d8744;box-shadow:1px 0 0 #c5d7a2}
.nav a:last-child{border:none;box-shadow:none}
.slider{position:absolute;left:10px;top:203px;width:940px;height:375px;background:#fff;border:1px solid #dcdcd6;padding:5px}
.slide{position:relative;width:930px;height:364px;background:linear-gradient(180deg,#9a8aa0 0%,#c7a09a 20%,#7d7f93 30%,#5d6a86 60%,#8c8a92 78%,#b5b0aa 100%)}
.caption{position:absolute;left:0;bottom:0;width:100%;height:60px;background:rgba(30,35,55,.8);color:var(--white);font-size:26px;text-align:center;line-height:60px}
.arrow{position:absolute;top:164px;width:35px;height:35px;background:rgba(20,20,20,.75)}
.arrow.prev{left:1px}.arrow.next{right:0}
.arrow svg{position:absolute;left:13px;top:12px}
.slider-shadow{position:absolute;left:200px;top:580px;width:560px;height:16px;background:radial-gradient(ellipse at top,rgba(0,0,0,.22),transparent 70%)}
h2{color:var(--green);font-weight:600}
.welcome h2{position:absolute;left:17px;top:618px;font-size:20px}
.team-photo{position:absolute;left:15px;top:655px;width:300px;height:128px;border:1px solid #ddd;padding:3px;background:#fff}
.team-photo div{width:100%;height:100%;background:linear-gradient(90deg,#5d7693,#a9b8cb 45%,#e6d8c8 70%,#f1f1f3)}
p{font-size:13px;line-height:20px}
.intro{position:absolute;left:336px;top:656px;width:296px}
.more-text{position:absolute;left:14px;top:801px;width:620px}
.btn{position:absolute;width:94px;height:28px;background:linear-gradient(#a7bf7a,#6f8b45);border:1px solid #5f783a;color:#1f2814;font-size:13px;line-height:27px;text-align:center}
.welcome .btn{left:13px;top:902px}
.divider{position:absolute;left:645px;top:622px;width:1px;height:235px;background:var(--rule)}
.services h2{position:absolute;left:665px;top:620px;font-size:22px;font-weight:400}
.services ul{position:absolute;left:668px;top:660px;list-style:none}
.services li{position:relative;padding-left:22px;font-size:13px;line-height:25.2px}
.services li::before{content:"›";position:absolute;left:0;top:-1px;font-weight:600;font-size:18px;color:var(--green-dark)}
.services .btn{left:668px;top:879px}
.footer-title{position:absolute;left:128px;top:1013px;font-size:22px;font-weight:600;color:var(--white)}
.address{position:absolute;left:126px;top:1048px;font-size:14px;line-height:24px;color:var(--white)}
.phone{position:absolute;right:130px;top:1016px;font-family:"PT Serif",serif;font-size:23px;color:var(--white);display:flex;align-items:center;gap:8px}
.email{position:absolute;right:128px;top:1056px;font-size:16px;font-style:italic;font-weight:600;color:var(--white);display:flex;align-items:center;gap:10px}
.footer-rule{position:absolute;left:128px;top:1118px;width:942px;height:1px;background:rgba(60,80,35,.5);box-shadow:0 1px 0 rgba(255,255,255,.2)}
.copyright{position:absolute;left:0;top:1140px;width:1200px;text-align:center;font-size:13px;color:var(--white)}
</style>
</head>
<body>
<div class="page">
  <div class="brand"><span class="brand-dot"></span><span class="brand-name">DRB</span></div>
  <div class="social" aria-label="Social links"><span></span><span></span><span></span><span></span></div>
  <div class="search"><em>Search here...</em>
    <svg width="26" height="22" viewBox="0 0 26 22"><circle cx="9" cy="8" r="6" fill="none" stroke="#7a8a55" stroke-width="2.5"/><line x1="13" y1="12" x2="22" y2="19" stroke="#7a8a55" stroke-width="4" stroke-linecap="round"/></svg>
  </div>
  <nav class="nav">
    <a style="width:100px">Home</a><a style="width:105px">Services</a><a style="width:118px">About Us</a><a style="width:219px">Product Specifications</a><a style="width:226px">Design Documentation</a><a style="width:126px">Contact Us</a>
  </nav>
  <div class="slider">
    <div class="slide" role="img" aria-label="Father and toddler holding hands on a beach at sunset">
      <div class="arrow prev"><svg width="8" height="10"><path d="M6 1L2 5l4 4" fill="none" stroke="#fff" stroke-width="1.3"/></svg></div>
      <div class="arrow next"><svg width="8" height="10"><path d="M2 1l4 4-4 4" fill="none" stroke="#fff" stroke-width="1.3"/></svg></div>
      <div class="caption">Rebuild Safer, Stronger, Better to build new lasting memories</div>
    </div>
  </div>
  <div class="slider-shadow"></div>

  <section class="welcome">
    <h2>Welcome to Our Site..</h2>
    <div class="team-photo"><div role="img" aria-label="Smiling businesswoman with colleagues in an office"></div></div>
    <p class="intro">Systems for extending the height of existing piles are not available on today’s market. Durable Raise Builders, LLC (DRB) has developed two systems to allow for Piles to be extended that provide superior structural support without corrosion and maintenance concerns.</p>
    <p class="more-text">We provided two systems, a complete system, Pile Cap Extension Tremlets, and Pile Splice. These two systems allow a home to be raised to by up to 54”, higher extensions possible with additional design consideration for lateral support. Shown below is the full Piling Extension system, which connects to the top of the existing pile. The system modular and can be cut to meet specific needs of the home.</p>
    <div class="btn">Read More</div>
  </section>

  <div class="divider"></div>

  <section class="services">
    <h2>Services</h2>
    <ul>
      <li>Sed ut perspiciatis unde omnis iste</li>
      <li>Error sit voluptatem accusantium</li>
      <li>Doloremque laudantium,</li>
      <li>Totam rem aperiam eaque</li>
      <li>Sed ut perspiciatis unde omnis iste</li>
      <li>Error sit voluptatem accusantium</li>
      <li>Doloremque laudantium,</li>
      <li>Totam rem aperiam eaque..</li>
    </ul>
    <div class="btn">Read More</div>
  </section>
</div>

<footer>
  <h3 class="footer-title">Contact Us</h3>
  <div class="address">Durable Raise Builders, LLC - PO Box 40312,<br>Harbor Vale, PA 18099</div>
  <div class="phone">
    <svg width="18" height="20" viewBox="0 0 18 20"><path d="M4 1l3 4-2 2c1 3 3 5 6 7l2-2 4 3-2 3C8 18 1 11 1 4z" fill="#c9d9ad"/></svg>
    (555) 014-2290
  </div>
  <div class="email">
    <svg width="24" height="14" viewBox="0 0 24 14"><rect x="1" y="1" width="22" height="12" fill="none" stroke="#c9d9ad" stroke-width="1.5"/><path d="M1 1l11 7 11-7" fill="none" stroke="#c9d9ad" stroke-width="1.5"/></svg>
    sales@durableraisebuilders.com
  </div>
  <div class="footer-rule"></div>
  <div class="copyright">©2013. DRB. All Right Reserved. Privacy Policy</div>
</footer>
</body>
</html>
```